Bus. Card/Envelope/Letterhead Design Request with my Logo

I have a logo created. I need to create a business card design, letterhead design and envelope design with the new logo.
Updates

The logo has now been posted. Thank you.

Target Market(s)

Professional. Legal Field.

Industry/Entity Type

Business

Requirements
Must have
• I like the same font as the logo.

```html
<!DOCTYPE html>
<html lang="en">
<head>
<meta charset="utf-8">
<title>Corrigan Whitlow LLP — Stationery Concepts</title>
<link rel="stylesheet" href="https://fonts.googleapis.com/css2?family=Cinzel:wght@400&family=Open+Sans:ital,wght@0,400;0,600;1,700&display=swap">
<style>
  :root{
    --stage:#9b9b9b;
    --paper:#ffffff;
    --charcoal:#2d2926;
    --green:#8aab26;
    --ink:#3a3a3a;
    --muted:#6a6a6a;
    --shadow:0 2px 5px rgba(0,0,0,.35);
  }
  *{box-sizing:border-box;margin:0;padding:0}
  html,body{width:1200px;height:806px;overflow:hidden}
  body{background:var(--stage);position:relative;font-family:"Open Sans",Arial,sans-serif;color:var(--ink)}
  .piece{position:absolute;box-shadow:var(--shadow)}

  /* wordmark */
  .mark{position:absolute;display:flex;flex-direction:column;align-items:center;font-family:"Cinzel",Georgia,serif}
  .mark-dot{width:14px;height:14px;border-radius:50%;background:var(--green);margin-bottom:4px}
  .mark-name{font-size:13px;letter-spacing:.3px;white-space:nowrap;line-height:1;padding:3px 0;border-top:1px solid currentColor;border-bottom:1px solid currentColor}
  .mark-tag{font-size:5.5px;letter-spacing:1.6px;margin-top:6px;white-space:nowrap}
  .mark.on-dark{color:#fff}
  .mark.on-dark .mark-dot{background:var(--green)}
  .mark.on-green{color:#fff}
  .mark.on-green .mark-dot{background:#fff}
  .mark.on-light{color:var(--ink)}

  .concepts-title{position:absolute;left:234px;top:83px;font-family:"Cinzel",Georgia,serif;font-size:15px;color:#2f2f2f;text-transform:none}

  /* business cards */
  .card{width:268px;height:150px}
  .card-front{left:38px;top:127px;background:var(--paper)}
  .card-back-a{left:314px;top:127px;background:var(--charcoal)}
  .card-back-b{left:38px;top:287px;background:var(--charcoal)}
  .card-back-c{left:314px;top:287px;background:var(--green)}
  .card-name{position:absolute;left:15px;top:33px;font-size:9.5px;font-weight:600;color:var(--green)}
  .card-address{position:absolute;left:15px;top:51px;font-size:6px;line-height:9.5px;color:var(--muted)}
  .contact-list{list-style:none}
  .contact-list li{display:flex;align-items:center;gap:5px;white-space:nowrap}
  .contact-list svg{width:7px;height:7px;fill:var(--green);flex:none}
  .card-contacts{position:absolute;left:15px;top:86px;font-size:6px;line-height:10.5px;color:var(--muted)}
  .card-rule{position:absolute;left:15px;right:13px;top:121px;border-top:1px solid var(--charcoal)}
  .card-web{position:absolute;left:15px;top:124px;font-size:6.5px;font-style:italic;font-weight:700;color:var(--ink)}

  /* envelope */
  .envelope{left:34px;top:448px;width:548px;height:316px;background:var(--paper);overflow:hidden}
  .envelope-flap{position:absolute;left:0;top:0;width:100%;height:79px;background:var(--charcoal);border-radius:12px 12px 0 0}
  .flap-web{position:absolute;left:0;right:0;top:18px;text-align:center;font-size:6.5px;font-style:italic;font-weight:700;color:#fff;transform:rotate(180deg)}
  .flap-dot{position:absolute;left:268px;top:36px;width:13px;height:13px;border-radius:50%;background:var(--green)}
  .envelope-return{position:absolute;left:40px;top:151px;font-size:7px;line-height:11px;color:var(--muted)}

  .foot-accent{position:absolute;left:0;right:0;bottom:11px;border-top:1.5px solid var(--green)}
  .foot-band{position:absolute;left:0;right:0;bottom:0;height:10px;background:var(--charcoal)}

  /* letterhead */
  .letterhead{left:609px;top:43px;width:557px;height:720px;background:var(--paper)}
  .lh-divider{position:absolute;left:377px;top:22px;height:80px;border-left:1px solid #cfcfcf}
  .lh-address{position:absolute;left:396px;top:22px;font-size:7.5px;line-height:12px;color:var(--muted)}
  .lh-contacts{position:absolute;left:396px;top:52px;font-size:7.5px;line-height:12.5px;color:var(--muted)}
  .lh-contacts svg{width:8px;height:8px}
</style>
</head>
<body>

<svg width="0" height="0" style="position:absolute" aria-hidden="true">
  <symbol id="i-phone" viewBox="0 0 10 10"><path d="M1 3.2C1 2 2.5 1 5 1s4 1 4 2.2v.6H7V3H3v.8H1z"/><rect x="2" y="4.5" width="6" height="4.5" rx=".6"/></symbol>
  <symbol id="i-fax" viewBox="0 0 10 10"><rect x="3" y="0.8" width="4" height="3"/><rect x="0.8" y="3.6" width="8.4" height="4" rx=".6"/><rect x="2.5" y="6.5" width="5" height="2.8"/></symbol>
  <symbol id="i-mail" viewBox="0 0 10 10"><path d="M.8 2h8.4v6H.8z M1.5 2.6 5 5.3l3.5-2.7" stroke="#fff" stroke-width=".6"/></symbol>
  <symbol id="i-web" viewBox="0 0 10 10"><circle cx="5" cy="5" r="4.2"/><path d="M.8 5h8.4M5 .8c-2 2.4-2 6 0 8.4M5 .8c2 2.4 2 6 0 8.4" stroke="#fff" stroke-width=".5" fill="none"/></symbol>
</svg>

<!-- presentation title -->
<div class="mark on-light" style="left:228px;top:22px">
  <span class="mark-dot" style="background:var(--charcoal)"></span>
  <span class="mark-name">Corrigan Whitlow LLP</span>
  <span class="mark-tag">ATTORNEYS AT LAW</span>
</div>
<div class="concepts-title">Stationary Concepts</div>

<!-- business card front -->
<section class="piece card card-front">
  <div class="card-name">Maeve Corrigan</div>
  <div class="card-address">2140 W. Harbor Blvd<br>Suite 310<br>Seaview, CA 90417</div>
  <ul class="contact-list card-contacts">
    <li><svg><use href="#i-phone"/></svg>310-555-0142</li>
    <li><svg><use href="#i-fax"/></svg>310-555-0187</li>
    <li><svg><use href="#i-mail"/></svg>maeve@cwattorneys.com</li>
  </ul>
  <div class="mark on-light" style="right:12px;top:106px">
    <span class="mark-name" style="border:none;padding:0;font-size:10px">Corrigan Whitlow LLP</span>
  </div>
  <div class="card-rule"></div>
  <div class="card-web">www.corriganwhitlow.com</div>
  <div class="mark-tag" style="position:absolute;left:163px;top:126px;font-family:'Cinzel',Georgia,serif;font-size:4.5px;letter-spacing:1.4px;color:var(--muted)">ATTORNEYS AT LAW</div>
</section>

<!-- business card backs -->
<section class="piece card card-back-a">
  <div class="mark on-dark" style="left:0;right:0;top:51px"><span class="mark-dot"></span><span class="mark-name">Corrigan Whitlow LLP</span><span class="mark-tag">ATTORNEYS AT LAW</span></div>
</section>
<section class="piece card card-back-b">
  <div class="mark on-dark" style="left:0;right:0;top:51px"><span class="mark-dot" style="background:#fff"></span><span class="mark-name">Corrigan Whitlow LLP</span><span class="mark-tag">ATTORNEYS AT LAW</span></div>
</section>
<section class="piece card card-back-c">
  <div class="mark on-green" style="left:0;right:0;top:51px"><span class="mark-dot"></span><span class="mark-name">Corrigan Whitlow LLP</span><span class="mark-tag">ATTORNEYS AT LAW</span></div>
</section>

<!-- envelope -->
<section class="piece envelope">
  <div class="envelope-flap">
    <div class="flap-web">www.corriganwhitlow.com</div>
    <span class="flap-dot"></span>
  </div>
  <div class="mark on-light" style="left:26px;top:96px"><span class="mark-dot"></span><span class="mark-name">Corrigan Whitlow LLP</span><span class="mark-tag">ATTORNEYS AT LAW</span></div>
  <div class="envelope-return">2140 W. Harbor Blvd, Suite 310<br>Seaview, CA 90417</div>
  <div class="foot-accent"></div>
  <div class="foot-band"></div>
</section>

<!-- letterhead -->
<section class="piece letterhead">
  <div class="mark on-light" style="left:32px;top:17px"><span class="mark-dot"></span><span class="mark-name">Corrigan Whitlow LLP</span><span class="mark-tag">ATTORNEYS AT LAW</span></div>
  <div class="lh-divider"></div>
  <div class="lh-address">2140 W. Harbor Blvd, Suite 310<br>Seaview, CA 90417</div>
  <ul class="contact-list lh-contacts">
    <li><svg><use href="#i-phone"/></svg>310-555-0142</li>
    <li><svg><use href="#i-fax"/></svg>310-555-0187</li>
    <li><svg><use href="#i-mail"/></svg>maeve@cwattorneys.com</li>
    <li><svg><use href="#i-web"/></svg>www.corriganwhitlow.com</li>
  </ul>
  <div class="foot-accent"></div>
  <div class="foot-band"></div>
</section>

</body>
</html>
```